Kaede Roasters

Full Shopify site .
About page

Merch page
Tshirts, hats, mugs

Coffee page
-sections
Single origin
Tomoe series
Sensu series
Decaf

KaedeX page
Cold brew
Coffee liquor
Absinthe Coffee

```html
<!DOCTYPE html>
<html lang="en">
<head>
<meta charset="utf-8">
<title>Kaede Roasters</title>
<link href="https://fonts.googleapis.com/css2?family=Poppins:wght@400;500;600&family=Tinos:wght@400;700&display=swap" rel="stylesheet">
<style>
:root{
  --red:#e8473f;
  --red-deep:#d63a33;
  --ink:#1c1b1b;
  --dark:#231f1d;
  --footer:#252322;
  --white:#ffffff;
  --muted:#cfcac6;
  --pink:#f6dfe0;
  --line:#8a3a34;
}
*{box-sizing:border-box;margin:0;padding:0}
html,body{width:1200px;height:4089px;overflow:hidden}
body{position:relative;background:var(--dark);font-family:"Poppins",sans-serif;color:var(--white)}
.abs{position:absolute}
.serif{font-family:"Tinos",serif;font-weight:700}
.btn{position:absolute;display:flex;align-items:center;justify-content:center;background:var(--red);color:var(--white);font-size:11px;font-weight:500;letter-spacing:.3px;text-transform:uppercase;border-radius:2px}

.topbar{left:0;top:0;width:1200px;height:38px;background:var(--red);font-size:12px;display:flex;align-items:center;justify-content:center;letter-spacing:.3px}
.header{left:0;top:38px;width:1200px;height:84px;background:var(--white);color:var(--ink)}
.brand{position:absolute;left:160px;top:18px;display:flex;align-items:center;gap:8px}
.brand-dot{width:40px;height:40px;border-radius:50%;background:var(--red)}
.brand-name{font-size:15px;font-weight:600;color:var(--ink);line-height:1.1}
.nav a{position:absolute;top:35px;font-size:12.5px;color:var(--ink);text-decoration:none}
.icon{position:absolute;top:30px}

.hero{left:0;top:122px;width:1200px;height:440px;background:linear-gradient(90deg,#1d232c 0%,#2b2a2c 45%,#3c3330 70%,#564640 100%)}
.hero h1{position:absolute;left:160px;top:238px;font-family:"Tinos",serif;font-weight:400;font-size:58px;line-height:58px}
.hero p{position:absolute;left:161px;top:366px;font-size:14.5px}

.beans{left:0;top:562px;width:1200px;height:881px;background:radial-gradient(ellipse at 50% 40%,#4a3126 0%,#2e201b 55%,#1e1816 100%)}
.about{left:160px;top:622px;width:878px;height:222px;background:var(--red);border-radius:3px}
.about h2{position:absolute;left:56px;top:45px;font-size:38px}
.about .lead{position:absolute;left:54px;top:96px;width:320px;font-size:13.5px;line-height:15px}
.about .body{position:absolute;left:421px;top:41px;width:418px;font-size:12.6px;line-height:17.8px}
.about .btn{left:54px;top:140px;width:129px;height:35px;background:var(--white);color:var(--ink)}

.h-sec{position:absolute;left:0;width:1200px;text-align:center;font-size:36px}
.card{position:absolute;top:989px;width:238px;height:327px;border:1px solid var(--line);border-radius:4px;background:rgba(30,22,20,.35)}
.stars{position:absolute;top:16px;left:0;width:100%;display:flex;justify-content:center;align-items:center;gap:2px;font-size:12px}
.stars svg{width:14px;height:14px}
.pack{position:absolute;left:59px;top:58px;width:120px;height:199px;border-radius:6px}
.card .name{position:absolute;top:278px;left:0;width:100%;text-align:center;font-size:17px;font-weight:600}

.banner{left:0;top:1443px;width:1200px;height:238px;background:linear-gradient(90deg,#7f98a6 0%,#9fb3bd 35%,#a9bac2 100%)}
.banner .photo{position:absolute;left:140px;top:0;width:340px;height:238px;background:linear-gradient(120deg,#8fa2ab 0%,#c2473f 60%,#b23a34 100%);opacity:.85}
.banner .line{position:absolute;left:509px;top:92px;font-size:39px}

.lower{left:0;top:1681px;width:1200px;height:2089px;background:radial-gradient(ellipse at 50% 60%,#2f2724 0%,#1f1b1a 70%)}
.tile{position:absolute;width:353px;height:440px}
.tile-label{position:absolute;font-size:16px;font-weight:600}
.tile-sub{position:absolute;font-size:11.5px;color:var(--muted)}
.arrow{position:absolute;width:22px;height:12px}

.news{left:49px;top:3185px;width:1100px;height:294px;background:rgba(70,58,52,.55);border-radius:14px}
.news input{position:absolute;left:254px;top:191px;width:417px;height:33px;border:none;border-radius:2px;padding-left:14px;font-family:"Poppins",sans-serif;font-size:12px;color:#555}
.news .btn{left:689px;top:191px;width:159px;height:33px;background:var(--white);color:var(--red);font-size:12px}

.footer{left:0;top:3770px;width:1200px;height:264px;background:var(--footer)}
.footer h4{position:absolute;top:49px;font-size:16px;font-weight:500}
.footer a{position:absolute;font-size:12px;color:var(--muted);text-decoration:none;line-height:15px}
.social{position:absolute;top:93px;width:18px;height:18px;border-radius:50%;border:2px solid var(--white)}
.paybar{left:0;top:4034px;width:1200px;height:55px;background:#1b1a19;display:flex;align-items:center;justify-content:center;gap:8px}
.pay{width:27px;height:17px;border-radius:2px;background:#e8e8e8}
</style>
</head>
<body>

<div class="abs topbar">WELCOME TO KAEDE ROASTERS</div>

<header class="abs header">
  <div class="brand"><span class="brand-dot"></span><span class="brand-name">Kaede<br>Roasters</span></div>
  <nav class="nav">
    <a style="left:373px">HOME</a>
    <a style="left:465px">ABOUT</a>
    <a style="left:561px">MERCH</a>
    <a style="left:662px">COFFEE</a>
    <a style="left:765px">KAEDEX</a>
  </nav>
  <svg class="icon" style="left:927px" width="20" height="20" viewBox="0 0 20 20" fill="none" stroke="#1c1b1b" stroke-width="1.8"><circle cx="8.5" cy="8.5" r="6"/><path d="M13 13l5 5"/></svg>
  <svg class="icon" style="left:972px" width="20" height="20" viewBox="0 0 20 20" fill="none" stroke="#1c1b1b" stroke-width="1.8"><circle cx="10" cy="6" r="4"/><path d="M2 19c0-5 4-7 8-7s8 2 8 7"/></svg>
  <svg class="icon" style="left:1013px;top:28px" width="28" height="24" viewBox="0 0 28 24" fill="none" stroke="#1c1b1b" stroke-width="1.8"><path d="M2 8h16l-1.5 13h-13z"/><path d="M6 8a4 4 0 0 1 8 0"/><circle cx="22" cy="5" r="4" fill="#e8473f" stroke="none"/></svg>
</header>

<section class="abs hero" role="img" aria-label="Night city skyline with a barista pouring coffee from a kettle into a cup, wearing a black branded T-shirt">
</section>
<h1 class="abs" style="left:160px;top:238px;font-family:'Tinos',serif;font-weight:400;font-size:58px;line-height:58px">Crafted Coffee.<br>Cultured Identity.</h1>
<p class="abs" style="left:161px;top:366px;font-size:14.5px">Single Origin Beans. Rare Blends. Designed Lifestyle.</p>
<a class="btn" style="left:160px;top:406px;width:129px;height:34px">Shop Coffee</a>
<a class="btn" style="left:298px;top:406px;width:151px;height:34px">Explore KaedeX</a>

<section class="abs beans" role="img" aria-label="Dark close-up of roasted coffee beans"></section>

<div class="abs about">
  <h2 class="serif">About Us</h2>
  <p class="lead">Stop overpaying at the cafe. It's easy to make cold brew at home.</p>
  <a class="btn">Learn More</a>
  <p class="body">It is a long established fact that a reader will be distracted by the readable content of a page when looking at its layout. The point of using Lorem Ipsum is that it has a more-or-less normal distribution of letters, as opposed to using 'Content here, content here', making it look like readable English. Many desktop publishing packages and web page editors now use Lorem Ipsum as their default model text, and a search for 'lorem ipsum' will uncover many web sites still in their infancy.</p>
</div>

<h2 class="h-sec serif" style="top:902px">Our Collections</h2>

<div class="card" style="left:97px">
  <div class="stars"><svg viewBox="0 0 20 20"><path fill="#e8473f" d="M10 1l2.7 6 6.3.6-4.8 4.3 1.4 6.4L10 15l-5.6 3.3 1.4-6.4L1 7.6 7.3 7z"/></svg><svg viewBox="0 0 20 20"><path fill="#e8473f" d="M10 1l2.7 6 6.3.6-4.8 4.3 1.4 6.4L10 15l-5.6 3.3 1.4-6.4L1 7.6 7.3 7z"/></svg><svg viewBox="0 0 20 20"><path fill="#e8473f" d="M10 1l2.7 6 6.3.6-4.8 4.3 1.4 6.4L10 15l-5.6 3.3 1.4-6.4L1 7.6 7.3 7z"/></svg><svg viewBox="0 0 20 20"><path fill="#e8473f" d="M10 1l2.7 6 6.3.6-4.8 4.3 1.4 6.4L10 15l-5.6 3.3 1.4-6.4L1 7.6 7.3 7z"/></svg><svg viewBox="0 0 20 20"><path fill="#e8473f" d="M10 1l2.7 6 6.3.6-4.8 4.3 1.4 6.4L10 15l-5.6 3.3 1.4-6.4L1 7.6 7.3 7z"/></svg>&nbsp;(10)</div>
  <div class="pack" role="img" aria-label="Single origin coffee bag, black with cream label" style="background:linear-gradient(180deg,#2a2a2a 0%,#2a2a2a 58%,#eee9e4 60%,#eee9e4 100%)"></div>
  <div class="name">Single Origin</div>
</div>
<div class="card" style="left:352px">
  <div class="stars"><svg viewBox="0 0 20 20"><path fill="#e8473f" d="M10 1l2.7 6 6.3.6-4.8 4.3 1.4 6.4L10 15l-5.6 3.3 1.4-6.4L1 7.6 7.3 7z"/></svg><svg viewBox="0 0 20 20"><path fill="#e8473f" d="M10 1l2.7 6 6.3.6-4.8 4.3 1.4 6.4L10 15l-5.6 3.3 1.4-6.4L1 7.6 7.3 7z"/></svg><svg viewBox="0 0 20 20"><path fill="#e8473f" d="M10 1l2.7 6 6.3.6-4.8 4.3 1.4 6.4L10 15l-5.6 3.3 1.4-6.4L1 7.6 7.3 7z"/></svg><svg viewBox="0 0 20 20"><path fill="#e8473f" d="M10 1l2.7 6 6.3.6-4.8 4.3 1.4 6.4L10 15l-5.6 3.3 1.4-6.4L1 7.6 7.3 7z"/></svg><svg viewBox="0 0 20 20"><path fill="#e8473f" d="M10 1l2.7 6 6.3.6-4.8 4.3 1.4 6.4L10 15l-5.6 3.3 1.4-6.4L1 7.6 7.3 7z"/></svg>&nbsp;(10)</div>
  <div class="pack" role="img" aria-label="Tomoe series coffee bag, white with red base" style="background:linear-gradient(180deg,#f3efec 0%,#f3efec 60%,#d8494a 85%,#b8363a 100%)"></div>
  <div class="name">Tomoe Series</div>
</div>
<div class="card" style="left:608px">
  <div class="stars"><svg viewBox="0 0 20 20"><path fill="#e8473f" d="M10 1l2.7 6 6.3.6-4.8 4.3 1.4 6.4L10 15l-5.6 3.3 1.4-6.4L1 7.6 7.3 7z"/></svg><svg viewBox="0 0 20 20"><path fill="#e8473f" d="M10 1l2.7 6 6.3.6-4.8 4.3 1.4 6.4L10 15l-5.6 3.3 1.4-6.4L1 7.6 7.3 7z"/></svg><svg viewBox="0 0 20 20"><path fill="#e8473f" d="M10 1l2.7 6 6.3.6-4.8 4.3 1.4 6.4L10 15l-5.6 3.3 1.4-6.4L1 7.6 7.3 7z"/></svg><svg viewBox="0 0 20 20"><path fill="#e8473f" d="M10 1l2.7 6 6.3.6-4.8 4.3 1.4 6.4L10 15l-5.6 3.3 1.4-6.4L1 7.6 7.3 7z"/></svg><svg viewBox="0 0 20 20"><path fill="#e8473f" d="M10 1l2.7 6 6.3.6-4.8 4.3 1.4 6.4L10 15l-5.6 3.3 1.4-6.4L1 7.6 7.3 7z"/></svg>&nbsp;(10)</div>
  <div class="pack" role="img" aria-label="Sensu series coffee bag, black with red band" style="background:linear-gradient(180deg,#2b2b2b 0%,#2b2b2b 62%,#9e2b2d 66%,#2b2b2b 72%,#2b2b2b 100%)"></div>
  <div class="name">Sensu Series</div>
</div>
<div class="card" style="left:863px">
  <div class="stars"><svg viewBox="0 0 20 20"><path fill="#e8473f" d="M10 1l2.7 6 6.3.6-4.8 4.3 1.4 6.4L10 15l-5.6 3.3 1.4-6.4L1 7.6 7.3 7z"/></svg><svg viewBox="0 0 20 20"><path fill="#e8473f" d="M10 1l2.7 6 6.3.6-4.8 4.3 1.4 6.4L10 15l-5.6 3.3 1.4-6.4L1 7.6 7.3 7z"/></svg><svg viewBox="0 0 20 20"><path fill="#e8473f" d="M10 1l2.7 6 6.3.6-4.8 4.3 1.4 6.4L10 15l-5.6 3.3 1.4-6.4L1 7.6 7.3 7z"/></svg><svg viewBox="0 0 20 20"><path fill="#e8473f" d="M10 1l2.7 6 6.3.6-4.8 4.3 1.4 6.4L10 15l-5.6 3.3 1.4-6.4L1 7.6 7.3 7z"/></svg><svg viewBox="0 0 20 20"><path fill="#e8473f" d="M10 1l2.7 6 6.3.6-4.8 4.3 1.4 6.4L10 15l-5.6 3.3 1.4-6.4L1 7.6 7.3 7z"/></svg>&nbsp;(10)</div>
  <div class="pack" role="img" aria-label="Decaf coffee bag, white with teal band" style="background:linear-gradient(180deg,#f3f3f1 0%,#f3f3f1 54%,#5a9a9a 58%,#f3f3f1 62%,#f3f3f1 100%)"></div>
  <div class="name">Decaf</div>
</div>

<a class="btn" style="left:513px;top:1362px;width:173px;height:35px">View All Collections</a>

<section class="abs banner">
  <div class="photo" role="img" aria-label="Woman in a red sweater drinking from a paper coffee cup against the sky"></div>
  <div class="line serif">Good days follow great&nbsp; coffee.</div>
</section>

<section class="abs lower" role="img" aria-label="Dark background with drifting coffee steam"></section>

<h2 class="h-sec serif" style="top:1738px">Limited Drops No Restocks</h2>

<div class="tile" style="left:49px;top:1833px;background:linear-gradient(180deg,var(--pink),#f1d3d5)" role="img" aria-label="Black branded T-shirt on a pink background"></div>
<div class="tile" style="left:424px;top:1833px;background:linear-gradient(180deg,var(--pink),#f1d3d5)" role="img" aria-label="Black branded cap on a pink background"></div>
<div class="tile" style="left:797px;top:1833px;background:linear-gradient(180deg,var(--pink),#f1d3d5)" role="img" aria-label="Black branded mug on a pink background"></div>

<div class="tile-label" style="left:49px;top:2292px">Tshirts</div>
<div class="tile-sub" style="left:49px;top:2313px">Comforting &amp; Rich</div>
<div class="tile-label" style="left:424px;top:2292px">Hats</div>
<div class="tile-sub" style="left:424px;top:2313px">Comforting &amp; Rich</div>
<div class="tile-label" style="left:797px;top:2292px">Mugs</div>
<div class="tile-sub" style="left:797px;top:2313px">Comforting &amp; Rich</div>
<svg class="arrow" style="left:380px;top:2307px" viewBox="0 0 22 12" fill="none" stroke="#fff" stroke-width="1.3"><path d="M0 6h21M16 1l5 5-5 5"/></svg>
<svg class="arrow" style="left:754px;top:2307px" viewBox="0 0 22 12" fill="none" stroke="#fff" stroke-width="1.3"><path d="M0 6h21M16 1l5 5-5 5"/></svg>
<svg class="arrow" style="left:1127px;top:2307px" viewBox="0 0 22 12" fill="none" stroke="#fff" stroke-width="1.3"><path d="M0 6h21M16 1l5 5-5 5"/></svg>

<a class="btn" style="left:513px;top:2371px;width:173px;height:35px">View All Collections</a>

<h2 class="h-sec serif" style="top:2457px">KaedeX</h2>

<div class="tile" style="left:49px;top:2552px;background:linear-gradient(180deg,#9a9793 0%,#6b4a36 55%,#8a6a48 100%)" role="img" aria-label="Iced cold brew with cream in a tall glass on a wooden board"></div>
<div class="tile" style="left:424px;top:2552px;background:linear-gradient(160deg,#6f5a3e 0%,#2a221c 50%,#cbbba4 100%)" role="img" aria-label="Glass mug of coffee liqueur with a cream top beside a bottle"></div>
<div class="tile" style="left:797px;top:2552px;background:linear-gradient(180deg,#1c1716 0%,#4a3529 50%,#b58d6c 75%,#2a1f1a 100%)" role="img" aria-label="Absinthe coffee in a tall champagne glass on a dark background"></div>

<div class="tile-label" style="left:49px;top:3016px">Cold Brew</div>
<div class="tile-label" style="left:424px;top:3016px">Coffee liquor</div>
<div class="tile-label" style="left:797px;top:3016px">Absinthe Coffee</div>
<svg class="arrow" style="left:380px;top:3022px" viewBox="0 0 22 12" fill="none" stroke="#fff" stroke-width="1.3"><path d="M0 6h21M16 1l5 5-5 5"/></svg>
<svg class="arrow" style="left:754px;top:3022px" viewBox="0 0 22 12" fill="none" stroke="#fff" stroke-width="1.3"><path d="M0 6h21M16 1l5 5-5 5"/></svg>
<svg class="arrow" style="left:1127px;top:3022px" viewBox="0 0 22 12" fill="none" stroke="#fff" stroke-width="1.3"><path d="M0 6h21M16 1l5 5-5 5"/></svg>

<a class="btn" style="left:513px;top:3090px;width:173px;height:35px">View All Collections</a>

<section class="abs news">
  <svg class="abs" style="left:524px;top:66px" width="52" height="36" viewBox="0 0 52 36" fill="none" stroke="#fff" stroke-width="2"><rect x="1" y="1" width="50" height="34"/><path d="M1 1l25 20L51 1M1 35l19-18M51 35L32 17"/></svg>
  <div class="abs serif" style="left:0;top:116px;width:1100px;text-align:center;font-size:40px">Subscribe to our newsletter</div>
  <input type="email" placeholder="Email address">
  <a class="btn">Subscribe</a>
</section>

<h2 class="h-sec serif" style="top:3541px;font-size:42px;line-height:54px">We Don't Just Sell Coffee.<br>We Build Rituals.</h2>
<a class="btn" style="left:520px;top:3676px;width:159px;height:35px">Shop Now</a>

<footer class="abs footer">
  <h4 style="left:160px">Quick Links</h4>
  <a style="left:160px;top:94px">About</a>
  <a style="left:160px;top:132px">Merch</a>
  <a style="left:160px;top:169px">Coffee</a>
  <a style="left:160px;top:207px">KaedeX</a>

  <h4 style="left:397px">Support</h4>
  <a style="left:397px;top:94px">FAQs</a>
  <a style="left:397px;top:132px">Contact Us:<br>support@kaederoasters.com</a>
  <a style="left:397px;top:184px">Phone: (888) 555-0142</a>

  <h4 style="left:665px">Company</h4>
  <a style="left:665px;top:94px">About Us</a>
  <a style="left:665px;top:132px">Contact</a>

  <h4 style="left:895px">Connect</h4>
  <span class="social" style="left:895px"></span>
  <span class="social" style="left:936px;border-radius:4px"></span>
  <span class="social" style="left:978px"></span>
  <span class="social" style="left:1020px;border-radius:4px"></span>
</footer>

<div class="abs paybar">
  <span class="pay"></span><span class="pay"></span><span class="pay"></span><span class="pay"></span><span class="pay"></span>
  <span class="pay"></span><span class="pay"></span><span class="pay"></span><span class="pay"></span><span class="pay"></span>
</div>

</body>
</html>
```